We want to design total new business card and logo for Kestrel Building Services Ltd

Our company name Kestrel Building Services Ltd. Design new logo and business card , need hi-end luxury style art for architecture and construction industry. The card should simple but stylish. Our business focus on CONNECT tradesman to construction company, help marketing construction company tender oversea projects, managing franchise in construction sector, delivery amazing services to our client, so Logo should show the CONNECTION IDEA, CONNECTING PEOPLE, LUXURY. Visit our website for more information: kestrelhub.co.nz

Low design quality

Target Market(s)

Directors or managers

Industry/Entity Type

Construction Company

Contact Information for Business Card

Name, Title, Mobile, Email, Website

Font styles to use
Serif

Colors

Designer to choose colors to be used in the design.

Requirements
Must have
• Simple and luxury, connection icon
Nice to have
• Special materials, plastic card, look through,...
• Look new ideas.

```html
<!DOCTYPE html>
<html lang="en">
<head>
<meta charset="utf-8">
<title>Kestrel Building Services Ltd – Business Card</title>
<link rel="stylesheet" href="https://fonts.googleapis.com/css2?family=Lora:wght@400;700&display=swap">
<style>
  :root {
    --backdrop: #5a4032;
    --teal: #02adcb;
    --white: #ffffff;
    --ink-grey: #6b6b6b;
    --text-font: "Lora", serif;
  }
  * { margin: 0; padding: 0; box-sizing: border-box; }
  html, body {
    width: 1200px;
    height: 848px;
    overflow: hidden;
    background: var(--backdrop);
  }
  .card {
    position: absolute;
    box-shadow: 0 4px 14px rgba(0, 0, 0, 0.35);
  }
  .card--front {
    left: 251px; top: 28px;
    width: 672px; height: 380px;
    background: var(--teal);
  }
  .card--back {
    left: 249px; top: 441px;
    width: 677px; height: 375px;
    background: var(--white);
  }
  .brand-square {
    position: absolute;
    display: block;
  }
  .card--front .brand-square {
    left: 296px; top: 118px;
    width: 80px; height: 80px;
    background: var(--white);
  }
  .card--back .brand-square {
    left: 209px; top: 150px;
    width: 40px; height: 40px;
    background: var(--teal);
  }
  .front-brand {
    position: absolute;
    left: 0; right: 0; top: 222px;
    text-align: center;
    font-family: var(--text-font);
    font-weight: 400;
    font-size: 34px;
    color: var(--white);
  }
  .back-brand {
    position: absolute;
    left: 80px; width: 298px; top: 208px;
    text-align: center;
    font-family: var(--text-font);
    font-weight: 400;
    font-size: 15.5px;
    color: var(--teal);
    white-space: nowrap;
  }
  .divider {
    position: absolute;
    left: 358px; top: 97px;
    width: 1.5px; height: 182px;
    background: var(--teal);
  }
  .contact {
    position: absolute;
    left: 380px; top: 90px;
    font-family: var(--text-font);
    color: var(--ink-grey);
    font-size: 16px;
    line-height: 22px;
    white-space: nowrap;
  }
  .contact__name {
    font-weight: 700;
    font-size: 19px;
    color: var(--teal);
    line-height: 24px;
  }
  .contact__title { margin-bottom: 16px; }
  .contact__address { margin-bottom: 16px; }
  .contact__line {
    display: flex;
    align-items: center;
    gap: 6px;
  }
  .contact__line svg { width: 14px; height: 14px; flex: none; }
</style>
</head>
<body>
  <section class="card card--front">
    <span class="brand-square" aria-hidden="true"></span>
    <p class="front-brand">Kestrel Building Services Ltd</p>
  </section>

  <section class="card card--back">
    <span class="brand-square" aria-hidden="true"></span>
    <p class="back-brand">Kestrel Building Services Ltd</p>
    <div class="divider"></div>
    <div class="contact">
      <p class="contact__name">Daniel Harper</p>
      <p class="contact__title">President</p>
      <p class="contact__address">18 Tawa street, Manurewa,<br>Auckland 2102, Newzealand</p>
      <p class="contact__line">
        <svg viewBox="0 0 14 14" aria-hidden="true"><path fill="#02adcb" d="M3 1.5 5 1l1.2 3-1.4 1a7 7 0 0 0 4.2 4.2l1-1.4L13 9l-.5 2c-.3.8-1.2 1.2-2 1A11 11 0 0 1 2 3.5c-.2-.8.2-1.7 1-2z"/></svg>
        0800 417265
      </p>
      <p class="contact__line">
        <svg viewBox="0 0 14 14" aria-hidden="true"><rect x="1" y="3.5" width="12" height="8" fill="#02adcb"/><path d="M1 3.5 7 8l6-4.5" fill="none" stroke="#fff" stroke-width="1"/></svg>
        info@kestrelhub.co.nz
      </p>
      <p class="contact__line">
        <svg viewBox="0 0 14 14" aria-hidden="true"><g fill="none" stroke="#02adcb" stroke-width="1"><circle cx="7" cy="7" r="5.5"/><ellipse cx="7" cy="7" rx="2.4" ry="5.5"/><path d="M1.5 7h11M2.5 4h9M2.5 10h9"/></g></svg>
        www.kestrelhub.co.nz
      </p>
    </div>
  </section>
</body>
</html>
```